ZipLOOM App logo & homescreen design

We are creating a new app call "ZipLOOM" that is designed for young adults (15-24 years old) to create a sexual risk reduction plan to help young adults follow their relationship goals while also being safe. Currently, we need graphic design for the ZipLOOM: (1) app logo and (2) a home screen for the app. We would like to see designs that are appealing to the target population - young adults ages 15-24. These requests are only the beginning of a series of graphic designs needs that I have to develop the app - and will offer one-on-one graphic design opportunities (much more $$$ to come) for the right graphic designer. The ZipLOOM app is complimentary follow-up to another commercial app we have call LANTERN, designed for doctors to assess young adults' level of sexual risk during a dr. appointment (see zilvoralabs.com for more details) after leaving a doctors visit. I have uploaded our company branding guidelines, but am open to any colors, fonts that are appealing to the target population.

Target Market(s)

youth 15-24 years of age

Industry/Entity Type

Health And Wellness

Colors

Designer to choose colors to be used in the design.

Requirements
Must have
• Both MUST be appealing to the target market.
• The app logo should be an icon or image that represents a plan.
• The homescreen UI needs to be easy to navigate and include 4 key sections: (1) Info - this section will include educational information tailored to their sexual risk level, (2) Plan - this section will link them to create their sexual risk reduction plan, (3) Sharing - this section will link them to areas that allow them to share their plan with their doctor or others, and (4) tip - this section may be a link OR the main part of the homescreen that shares daily/weekly tips on how to stick to their plan. I suggest getting inspiration from https://www.pixelquarry.com/30-recent-inspirational-ui-examples-in-mobile-device-screens.html.
Nice to have
• In app design focus groups, youth in the target market suggested that it would should have a similar look and feel to blinkwisp because they LOVE that app.
Should not have
• imply its a sexual related or healthcare/wellness related - want to to seem fun & easy to use. I open to any ideas here and am looking for YOU to be CREATIVE!!!

```html
<!DOCTYPE html>
<html lang="en">
<head>
<meta charset="utf-8">
<title>ZipLOOM – app screens</title>
<link rel="stylesheet" href="https://fonts.googleapis.com/css2?family=Josefin+Sans:wght@300;400;600;700&family=DM+Serif+Display&display=swap">
<style>
  :root{
    --page:#ffffff;
    --screen:#1b1a3a;
    --screen-deep:#17152f;
    --card:#211f45;
    --line:#3a3862;
    --label:#8c8aa8;
    --text:#ffffff;
    --muted:#c9c7dc;
    --purple:#7a2cc4;
    --pink:#d4246b;
    --violet:#5d52dd;
    --cyan:#33d1e6;
    --green:#3ec46d;
    --bar:#1d1c3f;
  }
  *{box-sizing:border-box;margin:0;padding:0}
  html,body{width:1200px;height:1200px;overflow:hidden;background:var(--page)}
  body{position:relative;font-family:"Josefin Sans",sans-serif;color:var(--text)}
  .screen{position:absolute;width:314px;height:558px;border-radius:20px;overflow:hidden;background:var(--screen);box-shadow:0 4px 14px rgba(0,0,0,.25)}
  .abs{position:absolute}
  .hero-photo{position:absolute;left:0;top:0;width:100%;height:260px;
    background:linear-gradient(180deg,#3a2e4a 0%,#413a5e 35%,#2e2f5a 60%,var(--screen) 100%)}
  .hero-photo::after{content:"";position:absolute;inset:0;background:radial-gradient(ellipse at 65% 30%,rgba(80,110,170,.45),transparent 60%)}
  .brand-name{position:absolute;left:0;width:100%;top:86px;text-align:center;font-weight:600;font-size:29px;letter-spacing:.5px}
  .brand-dot{display:block;margin:0 auto 10px;width:44px;height:44px;border:3px solid #fff;border-radius:50%}
  .form-card{position:absolute;background:var(--card);border-radius:6px;box-shadow:0 8px 20px rgba(0,0,0,.35)}
  .field-label{position:absolute;font-size:10px;letter-spacing:1px;color:var(--label);font-weight:600}
  .field-value{position:absolute;font-size:19px;font-weight:300}
  .field-line{position:absolute;height:1px;background:var(--line)}
  .dots{position:absolute;font-size:14px;letter-spacing:5px}
  .check{position:absolute;font-size:10px;font-weight:700}
  .tick{position:absolute;width:11px;height:11px}
  .btn{position:absolute;height:28px;border-radius:14px;background:var(--purple);text-align:center;font-weight:700;font-size:15px;line-height:31px}
  .link{position:absolute;width:100%;text-align:center;font-size:12px;font-weight:700}
  .ghost-pill{position:absolute;height:36px;border-radius:18px;background:var(--screen-deep);text-align:center;font-size:14px;line-height:39px;font-weight:300}
  .maker{position:absolute;left:0;width:100%;text-align:center;font-size:9px;font-weight:400;color:#fff}
  .maker i{display:inline-block;width:8px;height:8px;background:#fff;margin-right:3px;vertical-align:-1px}
  .tile{position:absolute;top:228px;width:90px;height:90px;border-radius:9px;background:#fff;color:#1b1a3a;text-align:center;font-size:12px}
  .tile svg{display:block;margin:26px auto 8px}
  .tip-title{position:absolute;left:16px;top:349px;font-size:15px}
  .tip-card{position:absolute;left:14px;top:374px;width:286px;height:132px;background:var(--card);border-radius:8px;padding:6px 20px}
  .tip-card h3{font-size:12px;font-weight:700;margin:4px 0 6px}
  .tip-card p{font-size:8.6px;line-height:14.4px;text-align:justify;color:#e6e5f0}
  .more{position:absolute;right:20px;top:532px;font-size:14px;letter-spacing:2px}
  .topbar-title{position:absolute;left:0;width:100%;top:37px;text-align:center;font-size:15px;font-weight:300}
  .menu-icon,.user-icon,.back-icon{position:absolute;top:36px}
  .menu-icon{left:24px}.back-icon{left:24px}.user-icon{right:24px}
  .topic{position:absolute;left:26px;width:268px;height:62px;border-radius:12px;background:var(--card);font-weight:700;font-size:15px;padding:0 38px;line-height:66px}
  .topic::after{content:"›";position:absolute;right:38px;top:-1px;font-size:18px;font-weight:400}
  .bottom-bar{position:absolute;left:0;bottom:0;width:100%;height:54px;background:var(--bar);display:flex;justify-content:space-around;align-items:center;padding:0 28px}
  .plan-label{position:absolute;font-size:12.5px;font-weight:300}
  .stars{position:absolute;font-size:9px;letter-spacing:1px}
  .tips-head{position:absolute;left:23px;font-family:"DM Serif Display",serif;font-size:25px;line-height:26px}
  .tips-photo{position:absolute;left:23px;width:167px}
  .tips-body{position:absolute;left:23px;width:276px;font-size:9.5px;line-height:14.5px;color:var(--muted)}
</style>
</head>
<body>

<!-- Login -->
<section class="screen" style="left:40px;top:18px">
  <div class="hero-photo" role="img" aria-label="Photo of a young person in denim, softly blurred"></div>
  <div class="brand-name" style="top:40px"><span class="brand-dot"></span>ZipLOOM</div>
  <div class="form-card" style="left:43px;top:173px;width:227px;height:222px">
    <div class="field-label" style="left:19px;top:23px">USERNAME</div>
    <div class="field-value" style="left:29px;top:55px">MiloRenner</div>
    <div class="field-line" style="left:19px;top:86px;width:190px"></div>
    <div class="field-label" style="left:19px;top:108px">PASSWORD</div>
    <div class="dots" style="left:27px;top:141px">●●●●●●●</div>
    <div class="field-line" style="left:19px;top:155px;width:190px"></div>
    <div class="check" style="left:55px;top:197px">☑ &nbsp;Keep me logged in</div>
  </div>
  <div class="btn" style="left:95px;top:364px;width:123px">Log in</div>
  <div class="link" style="top:446px">Forgot password ?</div>
  <div class="ghost-pill" style="left:43px;top:480px;width:227px">Register new user</div>
  <div class="maker" style="top:539px"><i></i>Halvaris Works</div>
</section>

<!-- Sign up -->
<section class="screen" style="left:443px;top:18px">
  <div class="hero-photo" role="img" aria-label="Photo of a young person in denim, softly blurred"></div>
  <div class="brand-name" style="top:40px"><span class="brand-dot"></span>ZipLOOM</div>
  <div class="form-card" style="left:42px;top:162px;width:227px;height:346px">
    <div class="field-label" style="left:19px;top:22px">FULL NAME</div>
    <div class="field-value" style="left:29px;top:52px">Milo Renner</div>
    <div class="field-line" style="left:19px;top:88px;width:190px"></div>
    <div class="field-label" style="left:19px;top:90px">USERNAME</div>
    <div class="field-value" style="left:29px;top:121px">MiloRenner</div>
    <svg class="tick" style="left:193px;top:132px" viewBox="0 0 12 12"><circle cx="6" cy="6" r="5" fill="none" stroke="var(--green)" stroke-width="1.3"/><path d="M3.5 6l2 2 3-4" fill="none" stroke="var(--green)" stroke-width="1.3"/></svg>
    <div class="field-line" style="left:19px;top:140px;width:190px"></div>
    <div class="field-label" style="left:19px;top:158px">PASSWORD</div>
    <div class="dots" style="left:27px;top:192px">●●●●●●●</div>
    <div class="field-line" style="left:19px;top:207px;width:190px"></div>
    <div class="field-label" style="left:19px;top:225px">DATE OF BIRTH</div>
    <div class="field-value" style="left:29px;top:256px;font-size:15px">18 April 1995</div>
    <svg class="tick" style="left:193px;top:268px" viewBox="0 0 12 12"><circle cx="6" cy="6" r="5" fill="none" stroke="var(--green)" stroke-width="1.3"/><path d="M3.5 6l2 2 3-4" fill="none" stroke="var(--green)" stroke-width="1.3"/></svg>
    <div class="field-line" style="left:19px;top:275px;width:190px"></div>
    <div class="check" style="left:32px;top:300px">☑ &nbsp;Accept Terms &amp; Conditions</div>
  </div>
  <div class="btn" style="left:94px;top:490px;width:125px">Sign in</div>
  <div class="maker" style="top:539px"><i></i>Halvaris Works</div>
</section>

<!-- Home -->
<section class="screen" style="left:844px;top:18px">
  <div class="hero-photo" role="img" aria-label="Photo of a young person in denim, softly blurred"></div>
  <div class="brand-name" style="top:40px"><span class="brand-dot"></span>ZipLOOM</div>
  <div class="tile" style="left:13px">
    <svg width="28" height="28" viewBox="0 0 24 24" fill="none" stroke="#1b1a3a" stroke-width="2"><path d="M3 3h18v13H9l-5 4V3z"/><path d="M12 7v5M12 14v.5"/></svg>Information</div>
  <div class="tile" style="left:112px">
    <svg width="28" height="28" viewBox="0 0 24 24" fill="none" stroke="#1b1a3a" stroke-width="2"><path d="M3 3v18h18"/><path d="M6 16l4-6 4 4 5-8"/></svg>Plan</div>
  <div class="tile" style="left:211px">
    <svg width="28" height="28" viewBox="0 0 24 24" fill="#1b1a3a" stroke="#1b1a3a" stroke-width="2"><circle cx="18" cy="5" r="2.5"/><circle cx="6" cy="12" r="2.5"/><circle cx="18" cy="19" r="2.5"/><path d="M8 11l8-5M8 13l8 5" fill="none"/></svg>Share</div>
  <div class="tip-title">💡︎ Tip of the day</div>
  <div class="tip-card">
    <h3>Act early</h3>
    <p>Field Notes Daily explains that 62 percent of teens who said that they drank reported they had their first drink before the age of 15 – not including simply taking a sip. This is why it is best for parents to talk to their kids about drugs and drinking around age 12, 13 or 14, since it is likely they will already have been offered substances by then.</p>
  </div>
  <div class="more" style="top:515px">●●●</div>
  <div class="maker" style="top:539px"><i></i>Halvaris Works</div>
</section>

<!-- Informations -->
<section class="screen" style="left:40px;top:613px">
  <div class="maker" style="top:16px"><i></i>Halvaris Works</div>
  <svg class="menu-icon" width="24" height="18" viewBox="0 0 24 18"><path d="M2 3h20M5 9h14M8 15h8" stroke="var(--cyan)" stroke-width="2.4" stroke-linecap="round"/></svg>
  <div class="topbar-title">Informations</div>
  <svg class="user-icon" width="20" height="22" viewBox="0 0 20 22" fill="none" stroke="var(--cyan)" stroke-width="2"><circle cx="10" cy="6" r="4"/><path d="M2 20c0-5 16-5 16 0" stroke="var(--pink)"/></svg>
  <div class="topic" style="top:80px">Alcohol use</div>
  <div class="topic" style="top:155px">Binge-drinking</div>
  <div class="topic" style="top:230px">Dangerous driving</div>
  <div class="topic" style="top:305px">Illegal substance use</div>
  <div class="topic" style="top:380px">Truancy</div>
  <div class="topic" style="top:455px">Tobacco smoking</div>
  <nav class="bottom-bar">
    <svg width="18" height="18" viewBox="0 0 24 24" fill="none" stroke="var(--violet)" stroke-width="2.2"><path d="M3 3h18v13H9l-5 4V3z"/><path d="M12 7v5M12 14v.5" stroke="var(--cyan)"/></svg>
    <svg width="18" height="18" viewBox="0 0 24 24" fill="none" stroke="#fff" stroke-width="2"><path d="M3 3v18h18"/><path d="M6 16l4-6 4 4 5-8"/></svg>
    <svg width="16" height="16" viewBox="0 0 24 24" fill="#fff" stroke="#fff" stroke-width="2"><circle cx="18" cy="5" r="2.5"/><circle cx="6" cy="12" r="2.5"/><circle cx="18" cy="19" r="2.5"/><path d="M8 11l8-5M8 13l8 5" fill="none"/></svg>
  </nav>
</section>

<!-- Problem solving -->
<section class="screen" style="left:443px;top:613px">
  <div class="maker" style="top:16px"><i></i>Halvaris Works</div>
  <svg class="back-icon" width="22" height="18" viewBox="0 0 22 18" fill="none" stroke="var(--violet)" stroke-width="2.2" stroke-linecap="round"><path d="M20 9H3M9 3L3 9l6 6"/></svg>
  <div class="topbar-title">Problem solving</div>
  <svg class="user-icon" width="20" height="22" viewBox="0 0 20 22" fill="none" stroke="var(--cyan)" stroke-width="2"><circle cx="10" cy="6" r="4"/><path d="M2 20c0-5 16-5 16 0" stroke="var(--pink)"/></svg>
  <div class="plan-label" style="left:30px;top:103px">My problem is</div>
  <div class="field-line" style="left:30px;top:146px;width:252px"></div>
  <div class="plan-label" style="left:30px;top:167px">Possible solutions</div>
  <div class="field-line" style="left:30px;top:210px;width:252px"></div>
  <div class="plan-label" style="left:30px;top:231px;color:var(--violet)">Pros</div>
  <div class="plan-label" style="left:160px;top:231px">Cons</div>
  <div class="field-line" style="left:30px;top:274px;width:122px"></div>
  <div class="field-line" style="left:160px;top:274px;width:122px"></div>
  <div class="stars" style="left:67px;top:282px;color:var(--violet)">★★★★☆</div>
  <div class="stars" style="left:197px;top:282px;color:var(--pink)">★★☆☆☆</div>
  <div class="plan-label" style="left:30px;top:315px">My solution is</div>
  <div class="field-line" style="left:30px;top:358px;width:252px"></div>
  <div class="plan-label" style="left:30px;top:379px">What we plan to do</div>
  <div class="field-line" style="left:30px;top:422px;width:252px"></div>
  <div class="plan-label" style="left:36px;top:445px">Date for review</div>
  <div class="plan-label" style="left:66px;top:473px">/ &nbsp; &nbsp; /</div>
  <div class="field-line" style="left:30px;top:485px;width:122px"></div>
  <div class="field-line" style="left:160px;top:485px;width:122px"></div>
  <nav class="bottom-bar">
    <svg width="18" height="18" viewBox="0 0 24 24" fill="none" stroke="#fff" stroke-width="2.2"><path d="M3 3h18v13H9l-5 4V3z"/><path d="M12 7v5M12 14v.5"/></svg>
    <svg width="18" height="18" viewBox="0 0 24 24" fill="none" stroke="var(--violet)" stroke-width="2"><path d="M3 3v18h18"/><path d="M6 16l4-6 4 4 5-8" stroke="var(--pink)"/></svg>
    <svg width="16" height="16" viewBox="0 0 24 24" fill="#fff" stroke="#fff" stroke-width="2"><circle cx="18" cy="5" r="2.5"/><circle cx="6" cy="12" r="2.5"/><circle cx="18" cy="19" r="2.5"/><path d="M8 11l8-5M8 13l8 5" fill="none"/></svg>
  </nav>
</section>

<!-- Tips -->
<section class="screen" style="left:844px;top:613px">
  <div class="maker" style="top:16px"><i></i>Halvaris Works</div>
  <svg class="menu-icon" width="24" height="18" viewBox="0 0 24 18"><path d="M2 3h20M5 9h14M8 15h8" stroke="var(--cyan)" stroke-width="2.4" stroke-linecap="round"/></svg>
  <div class="topbar-title">Tips</div>
  <svg class="user-icon" width="20" height="22" viewBox="0 0 20 22" fill="none" stroke="var(--cyan)" stroke-width="2"><circle cx="10" cy="6" r="4"/><path d="M2 20c0-5 16-5 16 0" stroke="var(--pink)"/></svg>
  <div class="tips-head" style="top:94px"><span style="color:var(--pink)">Being</span><br>a role model<br>for your child</div>
  <div class="tips-photo" role="img" aria-label="Photo of legs in jeans and pink sneakers against a rusty wall" style="top:181px;height:133px;background:linear-gradient(135deg,#7a3a1a,#b5652a 45%,#3f5f9c 70%,#c8a98a)"></div>
  <div class="tips-body" style="top:321px">Lorem ipsum dolor sit amet, consectetur adipisicing elit, sed do eiusmod tempor incididunt ut labore et dolore</div>
  <div class="tips-head" style="top:372px">Encouraging<br><span style="color:var(--violet)">good behaviour</span><br>in teenagers</div>
  <div class="tips-photo" role="img" aria-label="Photo of teenagers sitting on a car roof" style="top:456px;left:25px;height:50px;background:linear-gradient(180deg,#5a5f72,#2b2d3a)"></div>
  <nav class="bottom-bar">
    <svg width="18" height="18" viewBox="0 0 24 24" fill="none" stroke="var(--violet)" stroke-width="2.2"><path d="M3 3h18v13H9l-5 4V3z"/><path d="M12 7v5M12 14v.5" stroke="var(--cyan)"/></svg>
    <svg width="18" height="18" viewBox="0 0 24 24" fill="none" stroke="#fff" stroke-width="2"><path d="M3 3v18h18"/><path d="M6 16l4-6 4 4 5-8"/></svg>
    <svg width="16" height="16" viewBox="0 0 24 24" fill="#fff" stroke="#fff" stroke-width="2"><circle cx="18" cy="5" r="2.5"/><circle cx="6" cy="12" r="2.5"/><circle cx="18" cy="19" r="2.5"/><path d="M8 11l8-5M8 13l8 5" fill="none"/></svg>
  </nav>
</section>

</body>
</html>
```